Ridgewell Hauling Business Cards & Stantionery
Dump Truck Services
Ridgewell Hauling Business Cards & Stantionery -
Creative Brief
Professional
Osvaldo Mireles, Jr.
Owner
4158 Fenwick Rd. Pearland, TX 77590
osvaldo@ridgewellhauling-demo.com
www.ridgewellhauling-demo.com

```html
<!DOCTYPE html>
<html lang="en">
<head>
<meta charset="utf-8">
<title>Ridgewell Hauling Business Card</title>
<link href="https://fonts.googleapis.com/css2?family=Arimo:wght@400;700&display=swap" rel="stylesheet">
<style>
  :root {
    --backdrop: #e9e6e2;
    --card-white: #ffffff;
    --red-light: #c8282a;
    --red-mid: #a3181b;
    --red-deep: #6e0c0e;
    --brand-red: #c4161c;
    --swoosh-dark: #2a2a2a;
    --text-white: #ffffff;
    --shadow: rgba(0,0,0,0.25);
  }
  * { margin: 0; padding: 0; box-sizing: border-box; }
  html, body {
    width: 1200px; height: 422px; overflow: hidden;
    background: var(--backdrop);
    font-family: "Arimo", Arial, sans-serif;
  }
  .canvas { position: relative; width: 1200px; height: 422px; }
  .card {
    position: absolute; top: 53px; width: 518px; height: 336px;
    border-radius: 16px; overflow: hidden;
    box-shadow: 0 4px 12px var(--shadow);
  }
  .card-front {
    left: 72px;
    background: radial-gradient(ellipse at 70% 75%, var(--red-light) 0%, var(--red-mid) 45%, var(--red-deep) 100%);
  }
  .card-back { left: 632px; background: var(--card-white); }
  .swoosh { position: absolute; inset: 0; }
  .front-brand {
    position: absolute; left: 30px; top: 30px;
    display: flex; align-items: center; gap: 10px;
  }
  .brand-dot {
    flex-shrink: 0;
    width: 42px; height: 42px; border-radius: 50%;
    background: var(--brand-red);
  }
  .brand-name {
    font-weight: 700; color: var(--brand-red);
    text-transform: uppercase; line-height: 1; white-space: nowrap;
  }
  .front-brand .brand-name { font-size: 26px; }
  .address, .contact, .website {
    position: absolute; right: 22px; color: var(--text-white);
    font-size: 12.5px; line-height: 17px;
    text-align: right; white-space: nowrap;
  }
  .address { top: 150px; }
  .contact { top: 212px; }
  .website { top: 300px; }
  .holder { position: absolute; left: 22px; top: 232px; color: var(--text-white); white-space: nowrap; }
  .holder-name { font-size: 21px; font-weight: 400; }
  .holder-title { font-size: 12px; margin-top: 3px; }
  .back-brand {
    position: absolute; left: 50%; top: 50%;
    transform: translate(-50%, -50%);
    display: flex; align-items: center; gap: 14px;
  }
  .back-brand .brand-dot { width: 64px; height: 64px; }
  .back-brand .brand-name { font-size: 34px; }
</style>
</head>
<body>
<div class="canvas">
  <section class="card card-front">
    <svg class="swoosh" width="518" height="336" viewBox="0 0 518 336" aria-hidden="true">
      <path d="M0 0 H518 V100 C430 150 260 172 0 96 Z" fill="var(--card-white)"/>
      <path d="M30 108 C200 176 400 166 518 112" fill="none" stroke="var(--swoosh-dark)" stroke-width="5" stroke-linecap="round"/>
    </svg>
    <div class="front-brand">
      <span class="brand-dot"></span>
      <span class="brand-name">Ridgewell Hauling</span>
    </div>
    <div class="address">
      4158 Fenwick Rd.<br>
      Pearland, TX 77590
    </div>
    <div class="holder">
      <div class="holder-name">Osvaldo Mireles, Jr.</div>
      <div class="holder-title">Owner</div>
    </div>
    <div class="contact">
      C: (713) 555-0191<br>
      F: (281) 555-0147<br>
      E: osvaldo@ridgewellhauling-demo.com
    </div>
    <div class="website">W: www.ridgewellhauling-demo.com</div>
  </section>

  <section class="card card-back">
    <div class="back-brand">
      <span class="brand-dot"></span>
      <span class="brand-name">Ridgewell Hauling</span>
    </div>
  </section>
</div>
</body>
</html>
```